Meridale Crest Advisors – Franchise Growth & Development Presentation

Meridale Crest Advisors is an outsourced franchise sales organization (FSO) that helps franchisors grow their franchise systems without the expense and risk of hiring an internal franchise development team.

We are seeking a professional PowerPoint presentation that will be used to present our services to franchisors, franchise executives, founders, and growth-stage franchise brands.

The presentation should communicate the value of partnering with Meridale Crest Advisors, including:

• Fractional franchise sales team versus hiring internal staff
• 30+ years of franchise industry experience
• 550+ franchise sales successes
• Immediate access to established franchise broker relationships
• Proven franchise development processes
• Franchise growth strategy and enterprise value creation
• Potential private equity and exit opportunities through franchise expansion

The presentation should feel like a modern consulting, investment, or growth strategy presentation rather than a typical sales brochure. We want strong visual storytelling, custom infographics, professional diagrams, and clean business-oriented design.

The audience includes business owners, franchise founders, franchise executives, and investors who are evaluating growth strategies for their franchise systems.

Target Market(s)

Primary Audience: Emerging franchisors Growth-stage franchise brands Franchise founders Franchise CEOs Franchise presidents Franchise development executives Secondary Audience: Private equity firms Franchise investors Strategic buyers Franchise consultants

Industry/Entity Type

Franchise Development, Private Equity / Business Expansion

Font styles to use
Other font styles liked:
• Use Montserrat for titles and Open Sans for body text.

Requirements
Must have
• Modern professional business design Consistent branding throughout Custom infographics Comparison graphics Broker network ecosystem graphic Enterprise value graphic Easy-to-read charts and visuals Editable PowerPoint format Professional iconography. www.meridalecrestadvisors.example as reference for colors
Nice to have
• Franchise-related imagery Subtle growth-themed visuals Timeline graphics Data visualization Private equity / valuation style graphics
Should not have
• Cartoon graphics Clip art Overly busy slides Stock-template appearance Bright neon colors Handwritten fonts Excessive text on slides Juvenile or playful design elements

```html
<!DOCTYPE html>
<html lang="en">
<head>
<meta charset="UTF-8">
<title>Why Meridale Crest Advisors?</title>
<link href="https://fonts.googleapis.com/css2?family=Montserrat:wght@800&family=Inter:wght@400;500&display=swap" rel="stylesheet">
<style>
  :root {
    --navy: #1a3556;
    --navy-deep: #142b47;
    --ink: #0f2d4d;
    --orange: #f99b06;
    --card-light: #f6f6f6;
    --white: #ffffff;
  }
  * { margin: 0; padding: 0; box-sizing: border-box; }
  html, body { width: 1200px; height: 675px; overflow: hidden; background: var(--navy); }
  .slide {
    position: relative;
    width: 1200px;
    height: 675px;
    overflow: hidden;
  }
  .slide-backdrop {
    position: absolute;
    inset: 0;
    background:
      radial-gradient(ellipse at 30% 35%, rgba(40, 75, 115, 0.55), transparent 60%),
      linear-gradient(180deg, #1c3a5e 0%, var(--navy) 45%, var(--navy-deep) 100%);
  }
  .slide-title {
    position: absolute;
    top: 38px;
    left: 0;
    width: 100%;
    text-align: center;
    font-family: "Montserrat", sans-serif;
    font-weight: 800;
    font-size: 34px;
    line-height: 36px;
    color: var(--white);
    letter-spacing: 0.3px;
  }
  .slide-title .accent { color: var(--orange); }
  .feature-grid {
    position: absolute;
    top: 224px;
    left: 42.5px;
    display: grid;
    grid-template-columns: repeat(3, 354px);
    grid-template-rows: repeat(2, 194px);
    column-gap: 26.5px;
    row-gap: 26px;
  }
  .feature-card {
    position: relative;
    border-radius: 19px;
    background: var(--card-light);
  }
  .feature-card--accent { background: var(--orange); }
  .feature-icon {
    position: absolute;
    top: 20px;
    left: 50%;
    transform: translateX(-50%);
    width: 100px;
    height: 100px;
    color: var(--ink);
  }
  .feature-label {
    position: absolute;
    left: 0;
    width: 100%;
    top: 144px;
    text-align: center;
    font-family: "Inter", sans-serif;
    font-weight: 500;
    font-size: 19.5px;
    color: var(--ink);
  }
</style>
</head>
<body>
<main class="slide">
  <div class="slide-backdrop" role="img" aria-label="Dimmed office meeting room photograph in deep navy tones"></div>

  <h1 class="slide-title">WHY MERIDALE<br><span class="accent">CREST</span> ADVISORS?</h1>

  <section class="feature-grid">
    <article class="feature-card">
      <svg class="feature-icon" viewBox="0 0 100 100" fill="currentColor" aria-hidden="true">
        <circle cx="30" cy="16" r="9"/><circle cx="50" cy="12" r="10"/><circle cx="70" cy="16" r="9"/>
        <path d="M16 38a10 10 0 0 1 10-10h8v20H16z"/>
        <path d="M84 38a10 10 0 0 0-10-10h-8v20h18z"/>
        <rect x="36" y="26" width="28" height="22" rx="8"/>
        <rect x="16" y="52" width="68" height="5"/>
        <path d="M26 60h48a24 24 0 0 1-3 10l6 6-6 6-6-5a24 24 0 0 1-8 4v8h-14v-8a24 24 0 0 1-8-4l-6 5-6-6 6-6a24 24 0 0 1-3-10z"/>
        <path d="M38 60a12 12 0 0 0 24 0z" fill="var(--card-light)"/>
      </svg>
      <p class="feature-label">Fractional Team</p>
    </article>

    <article class="feature-card feature-card--accent">
      <svg class="feature-icon" viewBox="0 0 100 100" fill="currentColor" aria-hidden="true">
        <path d="M50 2l3.5 7.5 8 1-6 5.5 1.6 8L50 20l-7.1 4 1.6-8-6-5.5 8-1z"/>
        <path d="M24 18l3 6.5 7 .8-5.2 4.8 1.4 7-6.2-3.5-6.2 3.5 1.4-7-5.2-4.8 7-.8z"/>
        <path d="M76 18l3 6.5 7 .8-5.2 4.8 1.4 7-6.2-3.5-6.2 3.5 1.4-7-5.2-4.8 7-.8z"/>
        <path d="M34 70l-8 22 9-4 5 8 8-20zM66 70l8 22-9-4-5 8-8-20z"/>
        <circle cx="50" cy="60" r="24"/>
        <circle cx="50" cy="60" r="16" fill="var(--orange)"/>
        <circle cx="50" cy="60" r="13"/>
        <path d="M43 60l5 5 9-10" fill="none" stroke="var(--orange)" stroke-width="3.5" stroke-linecap="round" stroke-linejoin="round"/>
      </svg>
      <p class="feature-label">30+ Years of Experience</p>
    </article>

    <article class="feature-card">
      <svg class="feature-icon" viewBox="0 0 100 100" fill="currentColor" aria-hidden="true">
        <rect x="6" y="12" width="7" height="24" rx="3.5"/>
        <rect x="17" y="12" width="7" height="24" rx="3.5"/>
        <rect x="76" y="12" width="7" height="24" rx="3.5"/>
        <rect x="87" y="12" width="7" height="24" rx="3.5"/>
        <circle cx="50" cy="20" r="18"/>
        <circle cx="50" cy="20" r="14" fill="var(--card-light)"/>
        <circle cx="50" cy="20" r="12"/>
        <text x="50" y="27" text-anchor="middle" font-family="Inter, sans-serif" font-weight="600" font-size="19" fill="var(--card-light)">$</text>
        <path d="M6 42c7 4 12-4 17 0s12 4 17 0 12-4 17 0 12 4 17 0 12-4 20 0v50H6z"/>
        <rect x="17" y="56" width="22" height="26" fill="var(--card-light)"/>
        <rect x="23" y="62" width="10" height="14"/>
        <rect x="46" y="56" width="40" height="36" fill="var(--card-light)"/>
        <rect x="52" y="56" width="10" height="36"/><rect x="70" y="56" width="10" height="36"/>
        <rect x="6" y="84" width="40" height="8"/>
      </svg>
      <p class="feature-label">550+ Franchise Sales</p>
    </article>

    <article class="feature-card feature-card--accent">
      <svg class="feature-icon" viewBox="0 0 100 100" fill="currentColor" aria-hidden="true">
        <path d="M42 2h16l4 12 12-5 11 11-5 12 12 4v16l-12 4 5 12-11 11-12-5-4 12H42l-4-12-12 5-11-11 5-12-12-4V42l12-4-5-12 11-11 12 5z"/>
        <path d="M70 28c-10 0-20 6-26 16l-8 2-6 8 9 1 5 5 1 9 8-6 2-8c10-6 16-16 15-27z" fill="var(--orange)"/>
        <circle cx="60" cy="40" r="5"/>
        <path d="M36 62l-8 10 10-2z" fill="var(--orange)"/>
      </svg>
      <p class="feature-label">Immediate execution</p>
    </article>

    <article class="feature-card">
      <svg class="feature-icon" viewBox="0 0 100 100" fill="currentColor" aria-hidden="true">
        <circle cx="24" cy="20" r="16"/>
        <g fill="none" stroke="var(--card-light)" stroke-width="2.5">
          <ellipse cx="24" cy="20" rx="6" ry="15"/><line x1="9" y1="20" x2="39" y2="20"/><line x1="24" y1="5" x2="24" y2="35"/>
        </g>
        <path d="M64 6h10l3 4h15v28H64z"/>
        <rect x="64" y="14" width="28" height="2.5" fill="var(--card-light)"/>
        <rect x="36" y="24" width="30" height="46"/>
        <ellipse cx="24" cy="56" rx="22" ry="8"/>
        <rect x="2" y="56" width="44" height="32"/>
        <ellipse cx="24" cy="88" rx="22" ry="8"/>
        <g fill="none" stroke="var(--card-light)" stroke-width="2.5">
          <path d="M2 66c4 6 40 6 44 0M2 76c4 6 40 6 44 0"/>
        </g>
        <circle cx="80" cy="80" r="18"/>
        <circle cx="80" cy="80" r="14" fill="var(--card-light)"/>
        <circle cx="80" cy="75" r="5.5"/>
        <path d="M70 90a10 9 0 0 1 20 0z"/>
      </svg>
      <p class="feature-label">Proven Systems</p>
    </article>

    <article class="feature-card feature-card--accent">
      <svg class="feature-icon" viewBox="0 0 100 100" fill="currentColor" aria-hidden="true">
        <rect x="7" y="4" width="12" height="32" rx="4" transform="rotate(30 13 20)"/>
        <rect x="81" y="4" width="12" height="32" rx="4" transform="rotate(-30 87 20)"/>
        <path d="M24 22L40 14H58L78 22L86 40L66 60L54 70L30 58L16 42Z"/>
        <path d="M36 36L52 26L68 30" fill="none" stroke="var(--orange)" stroke-width="3.5" stroke-linecap="round" stroke-linejoin="round"/>
        <g stroke="var(--orange)" stroke-width="2.5">
          <circle cx="22" cy="50" r="7"/>
          <circle cx="30" cy="59" r="7"/>
          <circle cx="39" cy="67" r="7"/>
          <circle cx="49" cy="74" r="7"/>
        </g>
        <path d="M60 66L70 60M68 58L78 50" fill="none" stroke="var(--orange)" stroke-width="2.5" stroke-linecap="round"/>
      </svg>
      <p class="feature-label">Broker Network</p>
    </article>
  </section>
</main>
</body>
</html>
```